PingNearby

We are in need of a mobile app design including app and different icons.
- main page: to show
. asking or sharing (position, what I do, emotions, etc) with own contacts
. asking or sharing (what help I need) with subscribers around me
. Panic button (in case of emergency) that I can calll emergency services
(Police, Ambulance, Fire brigade, or
other personalized contacts (car relief, Insurance, my ICE contact)
Please refer to the attached PowerPoint for content and details. It shows the screens we need and explains about the branding and the approach we need.
Looking forward your proposals.

Reason: As I am new, I went for the proposed budget. Support team helped me better understand the systematic here :-)

Reason: I want to give a chance to a designer who submitted a proposal and I want to see his updated proposal per my input via email to him.

Target Market(s)

Yougsters and trendy people

Industry/Entity Type

Insurance

Font styles to use
Sans Serif

Colors
ffffff
9bcb3b

Requirements
Must have
• Should express: We are sharing, we are in a happy world, we keep in touch with each other, we are spontaneous.

Light green tendency (Brazilian light and shiny green) as a tendency.
Taking thins into account take chatlo a an inspiration from the popular apps (not talking about smilies, etc..., it is about their core design approach).
Nice to have
• design complicant sharing icons (e-mail, friendnest, chirpwave, SMS, etc)
Should not have
• Emergency look

```html
<!DOCTYPE html>
<html lang="en">
<head>
<meta charset="utf-8">
<title>PingNearby – app screens</title>
<link rel="stylesheet" href="https://fonts.googleapis.com/css2?family=Open+Sans:wght@400;600;700&family=Righteous&display=swap">
<style>
  :root {
    --bg: #eceef1;
    --white: #ffffff;
    --ink: #333333;
    --muted: #8a8a8a;
    --status: #111111;
    --splash-green: #16cc1e;
    --splash-light: #5fdc5a;
    --header-dark: #35a43a;
    --header-light: #7fd57a;
    --tab-green: #1cf03c;
    --tab-active: #12c42c;
    --tab-icon: #0b5e16;
    --brand-green: #9bcb3b;
    --brand-purple: #7b2fa8;
    --teal: #13b8a2;
    --yellow: #f5c31d;
    --grey-tile: #dedede;
    --map-grey: #9a9a9a;
    --map-green: #3fa33f;
    --seg-green: #3cc06a;
    --police: #1cb8f0;
    --police-dark: #1699c9;
    --amb: #f9e22c;
    --amb-dark: #d7c12a;
    --fire: #f25b50;
    --fire-dark: #d6483f;
    --input: #f0f0f0;
    --button: #5a5a5a;
  }
  * { box-sizing: border-box; margin: 0; padding: 0; }
  html, body { width: 1200px; height: 675px; overflow: hidden; }
  body { background: var(--bg); font-family: "Open Sans", sans-serif; color: var(--ink); position: relative; }

  .screen { position: absolute; top: 134px; width: 212px; height: 375px; background: var(--white); overflow: hidden; box-shadow: 0 1px 6px rgba(0,0,0,.08); }
  .screen--login { left: 69px; }
  .screen--home { left: 359px; }
  .screen--emergency { left: 645px; }
  .screen--contacts { left: 927px; }

  .status-bar { height: 12px; background: var(--status); color: var(--white); font-size: 7px; font-weight: 700; display: flex; align-items: center; justify-content: space-between; padding: 0 4px; }
  .status-bar__battery { width: 11px; height: 5px; border: 1px solid var(--white); }

  /* login */
  .splash { height: 218px; background: linear-gradient(120deg, var(--splash-green) 55%, var(--splash-light) 56%, var(--splash-green) 100%); display: flex; align-items: center; justify-content: center; }
  .splash__name { font-family: "Righteous", sans-serif; font-size: 24px; color: var(--brand-purple); }
  .field { position: absolute; left: 23px; width: 167px; height: 26px; background: var(--input); border: 1px solid #e2e2e2; font-size: 8px; color: #aaa; padding: 0 7px; display: flex; align-items: center; }
  .field--user { top: 246px; }
  .field--pass { top: 281px; letter-spacing: 1px; font-size: 10px; color: #888; }
  .btn-login { position: absolute; left: 39px; top: 319px; width: 134px; height: 26px; background: var(--button); color: var(--white); font-weight: 700; font-size: 11px; display: flex; align-items: center; justify-content: center; }

  /* header */
  .profile-bar { height: 42px; background: linear-gradient(120deg, var(--header-dark) 60%, var(--header-light) 61%, #9ce296 100%); display: flex; align-items: center; padding-left: 6px; color: var(--white); position: relative; }
  .avatar { width: 35px; height: 35px; border-radius: 50%; background: linear-gradient(#c89b7a, #8a6a52); border: 2px solid var(--white); flex: none; }
  .profile-bar__text { margin-left: 6px; line-height: 1; }
  .profile-bar__name { font-size: 14px; }
  .profile-bar__place { font-size: 9px; margin-top: 2px; }
  .profile-bar__brand { position: absolute; right: 6px; top: 15px; font-size: 8px; font-weight: 700; }

  /* tab bar */
  .tab-bar { position: absolute; left: 0; bottom: 0; width: 100%; height: 37px; background: var(--tab-green); display: flex; }
  .tab-bar__item { flex: 1; display: flex; align-items: center; justify-content: center; }
  .tab-bar__item--active { background: var(--tab-active); }
  .tab-bar svg { width: 16px; height: 16px; stroke: var(--tab-icon); fill: none; stroke-width: 1.6; }

  /* home tiles */
  .tile { position: absolute; color: var(--white); text-align: center; }
  .tile--friends { left: 9px; top: 104px; width: 93px; height: 85px; background: var(--teal); }
  .tile--people { left: 108px; top: 104px; width: 93px; height: 85px; background: var(--yellow); }
  .tile__icon { position: absolute; left: 50%; top: 14px; transform: translateX(-50%); }
  .tile__icon--people { width: 32px; height: 30px; background: #d6a414; border-radius: 3px; }
  .tile__title { position: absolute; left: 0; right: 0; top: 60px; font-size: 10px; }
  .tile__sub { position: absolute; left: 0; right: 0; top: 73px; font-size: 5px; }
  .tile--emergency { left: 8px; top: 195px; width: 195px; height: 85px; background: var(--grey-tile); color: #777; }
  .map { position: absolute; }
  .map--grey { left: 12px; top: 22px; width: 64px; height: 40px; background: var(--map-grey); border-radius: 6px 10px 14px 6px; }
  .tile--emergency .emergency-label { position: absolute; left: 96px; top: 22px; width: 90px; text-align: center; }
  .emergency-label__small { font-size: 9px; }
  .emergency-label__big { font-size: 16px; line-height: 1.1; }
  .emergency-label__note { font-size: 5px; margin-top: 3px; }

  /* segmented controls */
  .segmented { position: absolute; height: 20px; border: 1px solid var(--seg-green); border-radius: 10px; display: flex; overflow: hidden; font-size: 9px; color: var(--seg-green); }
  .segmented__option { flex: 1; display: flex; align-items: center; justify-content: center; }
  .segmented__option--active { background: var(--seg-green); color: var(--white); }
  .segmented--emergency { left: 19px; top: 66px; width: 171px; }
  .segmented--contacts { left: 7px; top: 63px; width: 200px; height: 21px; }

  .map--green { left: 24px; top: 111px; width: 70px; height: 40px; background: var(--map-green); border-radius: 6px 10px 14px 6px; }
  .screen--emergency .emergency-label { position: absolute; left: 115px; top: 114px; width: 80px; text-align: center; color: var(--map-green); }

  .services { position: absolute; left: 11px; top: 176px; width: 191px; height: 100px; display: flex; }
  .service { flex: 1; position: relative; color: var(--white); text-align: center; font-size: 8px; }
  .service--police { background: var(--police); }
  .service--amb { background: var(--amb); color: #6b6b1c; }
  .service--fire { background: var(--fire); }
  .service__figure { position: absolute; left: 16px; top: 18px; width: 32px; height: 40px; border-radius: 4px; }
  .service--police .service__figure { background: #0f6f99; }
  .service--amb .service__figure { background: #6a6a35; }
  .service--fire .service__figure { background: #8f2c26; }
  .service__mark { position: absolute; right: 3px; top: 3px; width: 13px; height: 13px; border-radius: 50%; background: var(--white); }
  .service__label { position: absolute; left: 0; right: 0; top: 69px; }
  .service__call { position: absolute; left: 0; right: 0; bottom: 0; height: 16px; line-height: 16px; font-size: 9px; }
  .service--police .service__call { background: var(--police-dark); }
  .service--amb .service__call { background: var(--amb-dark); color: var(--white); }
  .service--fire .service__call { background: var(--fire-dark); }

  /* contacts list */
  .contact-list { position: absolute; left: 18px; top: 105px; right: 8px; list-style: none; font-size: 9px; }
  .contact-list li { height: 24.5px; position: relative; }
  .contact-list__mark { position: absolute; right: 0; top: -6px; width: 17px; height: 17px; border-radius: 50%; background: var(--brand-green); }
</style>
</head>
<body>

<svg width="0" height="0" style="position:absolute">
  <defs>
    <symbol id="i-home" viewBox="0 0 16 16"><path d="M2 8 8 2.5 14 8M4 7v7h8V7"/></symbol>
    <symbol id="i-bell" viewBox="0 0 16 16"><path d="M4 11V7a4 4 0 0 1 8 0v4l1.5 1.5h-11zM6.5 14h3"/></symbol>
    <symbol id="i-book" viewBox="0 0 16 16"><rect x="3" y="2" width="10" height="12"/><circle cx="8" cy="7" r="1.8"/><path d="M5.5 11.5c.5-1.5 4.5-1.5 5 0"/></symbol>
    <symbol id="i-more" viewBox="0 0 16 16"><circle cx="3" cy="8" r="1.4"/><circle cx="8" cy="8" r="1.4"/><circle cx="13" cy="8" r="1.4"/></symbol>
  </defs>
</svg>

<!-- Login -->
<section class="screen screen--login">
  <div class="status-bar"><span>CARRIER</span><span class="status-bar__battery"></span></div>
  <div class="splash"><span class="splash__name">PingNearby</span></div>
  <div class="field field--user">User Name</div>
  <div class="field field--pass">•••••••••</div>
  <div class="btn-login">Login</div>
</section>

<!-- Home -->
<section class="screen screen--home">
  <div class="status-bar"><span>CARRIER</span><span class="status-bar__battery"></span></div>
  <header class="profile-bar">
    <div class="avatar" role="img" aria-label="Profile photo of Jonathan"></div>
    <div class="profile-bar__text"><div class="profile-bar__name">Jonathan</div><div class="profile-bar__place">Florida</div></div>
    <span class="profile-bar__brand">PingNearby</span>
  </header>
  <div class="tile tile--friends">
    <svg class="tile__icon" width="30" height="30" viewBox="0 0 30 30">
      <rect x="3" y="6" width="20" height="14" rx="2" fill="#f6f6f6" opacity=".9"/>
      <path d="M10 20l3 5 3-5z" fill="#f6f6f6" opacity=".9"/>
      <circle cx="9" cy="13" r="1.5" fill="#13b8a2"/><circle cx="13" cy="13" r="1.5" fill="#13b8a2"/><circle cx="17" cy="13" r="1.5" fill="#13b8a2"/>
      <circle cx="23" cy="7" r="5" fill="#e8242a"/>
      <text x="23" y="9.5" font-size="7" fill="#fff" text-anchor="middle" font-family="Open Sans, sans-serif">2</text>
    </svg>
    <div class="tile__title">Tell Friends</div>
    <div class="tile__sub">position, what I do, emotions, etc</div>
  </div>
  <div class="tile tile--people">
    <div class="tile__icon tile__icon--people" role="img" aria-label="Icon of people around the user"></div>
    <div class="tile__title">Tell Peoples</div>
    <div class="tile__sub">with subscribers around me</div>
  </div>
  <div class="tile tile--emergency">
    <div class="map map--grey" role="img" aria-label="Map of the USA"></div>
    <div class="emergency-label">
      <div class="emergency-label__small">Emergency</div>
      <div class="emergency-label__big">USA</div>
      <div class="emergency-label__note">Police, Ambulance, Fire brigade</div>
    </div>
  </div>
  <nav class="tab-bar">
    <div class="tab-bar__item tab-bar__item--active"><svg><use href="#i-home"/></svg></div>
    <div class="tab-bar__item"><svg><use href="#i-bell"/></svg></div>
    <div class="tab-bar__item"><svg><use href="#i-book"/></svg></div>
    <div class="tab-bar__item"><svg><use href="#i-more"/></svg></div>
  </nav>
</section>

<!-- Emergency -->
<section class="screen screen--emergency">
  <div class="status-bar"><span>CARRIER</span><span class="status-bar__battery"></span></div>
  <header class="profile-bar">
    <div class="avatar" role="img" aria-label="Profile photo of Jonathan"></div>
    <div class="profile-bar__text"><div class="profile-bar__name">Jonathan</div><div class="profile-bar__place">Florida</div></div>
    <span class="profile-bar__brand">PingNearby</span>
  </header>
  <div class="segmented segmented--emergency">
    <div class="segmented__option">Friends</div>
    <div class="segmented__option segmented__option--active">Circle</div>
  </div>
  <div class="map map--green" role="img" aria-label="Map of the USA"></div>
  <div class="emergency-label">
    <div class="emergency-label__small">Emergency</div>
    <div class="emergency-label__big">USA</div>
  </div>
  <div class="services">
    <div class="service service--police">
      <div class="service__figure" role="img" aria-label="Police officer icon"></div>
      <span class="service__mark"></span>
      <div class="service__label">Police</div>
      <div class="service__call">Call</div>
    </div>
    <div class="service service--amb">
      <div class="service__figure" role="img" aria-label="Ambulance icon"></div>
      <div class="service__label">Ambulance</div>
      <div class="service__call">Call</div>
    </div>
    <div class="service service--fire">
      <div class="service__figure" role="img" aria-label="Fire truck icon"></div>
      <div class="service__label">Fire Bridge</div>
      <div class="service__call">Call</div>
    </div>
  </div>
  <nav class="tab-bar">
    <div class="tab-bar__item tab-bar__item--active"><svg><use href="#i-home"/></svg></div>
    <div class="tab-bar__item"><svg><use href="#i-bell"/></svg></div>
    <div class="tab-bar__item"><svg><use href="#i-book"/></svg></div>
    <div class="tab-bar__item"><svg><use href="#i-more"/></svg></div>
  </nav>
</section>

<!-- Contacts -->
<section class="screen screen--contacts">
  <div class="status-bar"><span>CARRIER</span><span class="status-bar__battery"></span></div>
  <header class="profile-bar">
    <div class="avatar" role="img" aria-label="Profile photo of Jonathan"></div>
    <div class="profile-bar__text"><div class="profile-bar__name">Jonathan</div><div class="profile-bar__place">Florida</div></div>
  </header>
  <div class="segmented segmented--contacts">
    <div class="segmented__option">All</div>
    <div class="segmented__option">Group</div>
    <div class="segmented__option segmented__option--active">Emergency</div>
  </div>
  <ul class="contact-list">
    <li>Mila Varenko<span class="contact-list__mark"></span></li>
    <li>Tomas Reyl</li>
    <li>RoadAid from abroad</li>
    <li>Alpenhof Insurance</li>
    <li>Credit card company</li>
    <li>Embassy</li>
  </ul>
  <nav class="tab-bar">
    <div class="tab-bar__item"><svg><use href="#i-home"/></svg></div>
    <div class="tab-bar__item"><svg><use href="#i-bell"/></svg></div>
    <div class="tab-bar__item tab-bar__item--active"><svg><use href="#i-book"/></svg></div>
    <div class="tab-bar__item"><svg><use href="#i-more"/></svg></div>
  </nav>
</section>

</body>
</html>
```